New Digital Marketing Company Needs Web Design

Introduction

Brightcrest gives advice to small businesses about their websites and digital marketing strategies and builds working relationships with clients to understand their business and maximise its online presence.

Brightcrest offers services to support its clients needs such as: website auditing & search engine optimisation (SEO), Quorvo Promoline, Chatterlane advertising, newsletter development & management, online performance reporting, email setup & management, website hosting, maintenance & backup, web development, web updates & web design.

Design Specification

The site should have a clean & professional look and use the colour scheme from the logo (attached below).

The design should consist of 2 templates; The homepage & content page.

Homepage Design

The homepage should have a header with logo, contact number and email and menu. Followed underneath by a slider and then individual blocks for key services. Under the key services should be a testimonial block with 3 testimonials. Finally the footer with company details, menu links and location map.

Header Info:

Contact number: 01632 960481
Email: info@brightcrest-demo.co.uk

Menu: Home Services About Contact

Slider Design:

The slider should be full page and show an image with text.

Key Services:

The key services should have a relevant icon and brief description.

The key services are:

Digital Marketing

Website Hosting & Management

Website Health Check (SEO)

Website Updating & Development

Newsletter Management

Email Management

Note: Lorem Ipsum can be used for brief description...

Testimonials:

There should be 3 testimonials side by side and they should include a headshot image of the person giving the testimonial.

Note: Lorem Ipsum and sample images can be used for testimonials...

Footer:

The footer should have 3 sections:

Menu links:

Digital Marketing About
Quorvo Promoline Contact
Chatterlane Advertising Privacy Policy
Search Engine Optimisation (SEO) Terms & Conditions
Website Hosting FAQ
Newsletter Management

Company Information:

BrightCrest
14 Marlow Close
Eastmere
Berskhire
ZZ9 4QT
Tel: 01632 960481

Chatterlane icon - Pipwave icon - Careernest icon

Location

Quorvo map

Footer Bottom:

Copyright message.

Content Design

The content design should have the common header and footer.

Each content page should have a banner for image with text description (page title).

The content page should have area for text description and area for a video display if available.

There should be a right column (possibly) for modules (latest blog, latest Chatterlane feeds, testimonial)

Project Deadline Extended
Reason: I have had to extend the deadline as could not review while on vacation and need to feedback to some designers for content page design. Many thanks for your understanding.

Target Market(s)

Industry/Entity Type

Digital

Number of Pages Required

2 page

Requirements
Must have
• The site should have a clean & professional look and use the colour scheme from the logo (attached below).
• The design should consist of 2 templates; The homepage & content page.

```html
<!DOCTYPE html>
<html lang="en">
<head>
<meta charset="utf-8">
<title>BrightCrest – Home</title>
<link href="https://fonts.googleapis.com/css2?family=Open+Sans:wght@400;600;700;800&display=swap" rel="stylesheet">
<style>
:root{
  --purple:#5a3f7a;
  --purple-deep:#3f2a58;
  --berry:#7b1743;
  --ink:#333;
  --muted:#777;
  --line:#e3e3e3;
  --dark:#3b3b3d;
  --footer:#f1f1f1;
  --white:#fff;
}
*{margin:0;padding:0;box-sizing:border-box}
html,body{width:758px;height:1200px;overflow:hidden}
body{font-family:"Open Sans",Arial,sans-serif;color:var(--ink);background:var(--white);position:relative}
.wrap{width:680px;margin:0 auto;position:relative}

/* header + hero */
.hero{position:relative;height:396px;background:linear-gradient(120deg,#7d6a93 0%,#6a5683 45%,#8a7a9c 100%)}
.hero-photo{position:absolute;inset:0;background:linear-gradient(100deg,rgba(90,63,122,.85) 0%,rgba(90,63,122,.7) 55%,rgba(140,125,160,.55) 100%)}
.site-header{position:relative;height:40px;background:rgba(40,24,58,.55)}
.site-header .wrap{display:flex;align-items:center;height:40px}
.brand{display:flex;align-items:center;gap:6px;font-weight:700;font-size:14px;color:var(--white)}
.brand-dot{width:15px;height:15px;border-radius:50%;background:var(--berry)}
.contact{display:flex;gap:26px;margin-left:90px;font-size:7.5px;color:var(--white)}
.contact span{display:flex;align-items:center;gap:5px}
.menu{margin-left:auto;display:flex;gap:34px;font-size:7.5px;font-weight:600;color:var(--white);letter-spacing:.5px}
.hero-text{position:relative;padding-top:80px}
.hero-text h1{font-size:26px;font-weight:800;color:var(--white);letter-spacing:.3px}
.hero-text h2{font-size:13px;font-weight:600;color:var(--white);margin-top:4px}
.hero-text p{font-size:7.5px;line-height:1.6;color:#eee;width:300px;margin-top:12px}
.slider-bar{height:22px;background:#ececec;position:relative}
.dots{position:absolute;right:40px;top:8px;display:flex;gap:5px}
.dots i{width:6px;height:6px;border-radius:50%;background:#bbb}
.dots i.on{background:var(--berry)}

/* help */
.help{padding-top:30px}
.help h3{font-size:11px;font-weight:600;color:var(--ink)}
.help h3 b{color:var(--berry)}
.help-underline{width:30px;height:2px;background:var(--berry);margin:5px 0 8px}
.help-row{display:flex;justify-content:space-between;align-items:flex-start}
.help-row p{width:300px;font-size:6.5px;line-height:1.6;color:var(--muted)}
.btn{background:var(--berry);color:var(--white);font-size:7.5px;font-weight:700;padding:9px 38px;letter-spacing:.5px}
.services{display:grid;grid-template-columns:repeat(3,1fr);gap:22px 22px;margin-top:20px;padding-top:14px;border-top:1px solid var(--line)}
.service{padding-bottom:12px;border-bottom:1px solid var(--line)}
.service-head{display:flex;align-items:center;gap:7px}
.service-icon{width:20px;height:20px;background:var(--purple);display:flex;align-items:center;justify-content:center}
.service h4{font-size:6.5px;font-weight:700;color:var(--purple);text-transform:uppercase}
.service p{font-size:6px;line-height:1.6;color:var(--muted);margin-top:7px}

/* clients */
.clients{position:absolute;top:718px;left:0;width:758px;height:114px;background:var(--dark)}
.clients .wrap{display:flex;justify-content:space-between;padding-top:14px}
.clients h3{font-size:10px;font-weight:700;color:var(--white)}
.clients p{font-size:6.5px;line-height:1.6;color:#bbb;width:280px;margin-top:8px}
.client-names{display:flex;gap:34px;align-items:center;margin-top:26px}
.client-names span{font-size:14px;font-weight:700;color:#ddd}
.testimonials{position:absolute;top:850px;left:0;width:758px}
.testimonials .wrap{display:flex;justify-content:space-between}
.quote{width:205px;display:flex;gap:10px}
.headshot{width:44px;height:44px;border-radius:50%;flex:none;background:linear-gradient(135deg,#c9b8a8,#8e7b6c)}
.quote h5{font-size:6.5px;font-weight:700;color:var(--ink)}
.quote h5 span{color:var(--berry)}
.quote p{font-size:6px;line-height:1.6;color:var(--muted);margin-top:4px}

/* footer */
.site-footer{position:absolute;top:955px;left:0;width:758px;height:212px;background:var(--footer)}
.site-footer .wrap{display:flex;padding-top:24px}
.links{font-size:6px;line-height:2.1;color:#666;width:120px}
.links-short{width:80px;margin-left:20px}
.company{width:150px;margin-left:30px}
.company .brand{color:var(--purple);font-size:12px}
.company p{font-size:6px;line-height:1.8;color:#666;margin-top:6px}
.socials{display:flex;gap:6px;margin-top:8px}
.socials i{width:11px;height:11px;border-radius:50%;background:var(--purple)}
.map{margin-left:auto;width:260px;height:150px;background:linear-gradient(135deg,#e4e6e0,#d7dbd3);position:relative}
.map svg{position:absolute;left:122px;top:52px}
.bottom-bar{position:absolute;top:1167px;left:0;width:758px;height:33px;background:var(--dark)}
.bottom-bar .wrap{display:flex;justify-content:space-between;font-size:6px;color:#aaa;padding-top:13px}
</style>
</head>
<body>

<section class="hero">
  <div class="hero-photo" role="img" aria-label="Photo of a team at work in an office, tinted purple"></div>
  <header class="site-header">
    <div class="wrap">
      <div class="brand"><span class="brand-dot"></span>BrightCrest</div>
      <div class="contact">
        <span><svg width="8" height="8" viewBox="0 0 10 10"><path d="M2 1l2 2-1 1.5c.6 1.2 1.3 1.9 2.5 2.5L7 6l2 2-1.5 1.5C4 9 1 6 .5 2.5z" fill="#fff"/></svg>01632 960481</span>
        <span><svg width="9" height="7" viewBox="0 0 10 8"><rect x=".5" y=".5" width="9" height="7" fill="none" stroke="#fff"/><path d="M.5.5l4.5 4 4.5-4" fill="none" stroke="#fff"/></svg>info@brightcrest-demo.co.uk</span>
      </div>
      <nav class="menu"><span>HOME</span><span>SERVICES</span><span>ABOUT</span><span>CONTACT</span></nav>
    </div>
  </header>
  <div class="wrap hero-text">
    <h1>UNDERSTAND YOUR BUSINESS</h1>
    <h2>MAXIMISE ITS ONLINE PRESENCE</h2>
    <p>BrightCrest gives advice to small businesses about their websites and digital marketing strategies and builds working relationships with clients to understand their business and maximise its online presence.</p>
  </div>
</section>
<div class="slider-bar"><div class="dots"><i class="on"></i><i></i><i></i></div></div>

<section class="help">
  <div class="wrap">
    <h3>HOW <b>WE</b> CAN HELP</h3>
    <div class="help-underline"></div>
    <div class="help-row">
      <p>Lorem ipsum dolor sit amet, consectetur adipiscing elit, sed do eiusmod tempor incididunt ut labore et dolore magna aliqua. Ut enim ad minim veniam, quis nostrud exercitation.</p>
      <span class="btn">GET IN TOUCH</span>
    </div>
    <div class="services">
      <div class="service"><div class="service-head"><span class="service-icon"><svg width="12" height="12" viewBox="0 0 12 12"><path d="M1 11V7h2v4zm3 0V4h2v7zm3 0V1h2v10z" fill="#fff"/></svg></span><h4>Digital Marketing</h4></div><p>Lorem ipsum dolor sit amet, consectetur adipiscing elit, sed do eiusmod tempor incididunt ut labore et dolore magna aliqua.</p></div>
      <div class="service"><div class="service-head"><span class="service-icon"><svg width="12" height="12" viewBox="0 0 12 12"><rect x="1" y="1" width="10" height="4" fill="#fff"/><rect x="1" y="7" width="10" height="4" fill="#fff"/></svg></span><h4>Website Hosting &amp; Management</h4></div><p>Lorem ipsum dolor sit amet, consectetur adipiscing elit, sed do eiusmod tempor incididunt ut labore et dolore magna aliqua.</p></div>
      <div class="service"><div class="service-head"><span class="service-icon"><svg width="12" height="12" viewBox="0 0 12 12"><circle cx="5" cy="5" r="3.5" fill="none" stroke="#fff" stroke-width="1.5"/><path d="M7.5 7.5L11 11" stroke="#fff" stroke-width="1.5"/></svg></span><h4>Website Health Check (SEO)</h4></div><p>Lorem ipsum dolor sit amet, consectetur adipiscing elit, sed do eiusmod tempor incididunt ut labore et dolore magna aliqua.</p></div>
      <div class="service"><div class="service-head"><span class="service-icon"><svg width="12" height="12" viewBox="0 0 12 12"><path d="M4 3L1 6l3 3M8 3l3 3-3 3" fill="none" stroke="#fff" stroke-width="1.5"/></svg></span><h4>Website Updating &amp; Development</h4></div><p>Lorem ipsum dolor sit amet, consectetur adipiscing elit, sed do eiusmod tempor incididunt ut labore et dolore magna aliqua.</p></div>
      <div class="service"><div class="service-head"><span class="service-icon"><svg width="12" height="12" viewBox="0 0 12 12"><rect x="2" y="1" width="8" height="10" fill="none" stroke="#fff" stroke-width="1.3"/><path d="M4 4h4M4 6h4M4 8h3" stroke="#fff"/></svg></span><h4>Newsletter Management</h4></div><p>Lorem ipsum dolor sit amet, consectetur adipiscing elit, sed do eiusmod tempor incididunt ut labore et dolore magna aliqua.</p></div>
      <div class="service"><div class="service-head"><span class="service-icon"><svg width="12" height="10" viewBox="0 0 12 10"><rect x=".7" y=".7" width="10.6" height="8.6" fill="none" stroke="#fff" stroke-width="1.3"/><path d="M1 1l5 4 5-4" fill="none" stroke="#fff" stroke-width="1.3"/></svg></span><h4>Email Management</h4></div><p>Lorem ipsum dolor sit amet, consectetur adipiscing elit, sed do eiusmod tempor incididunt ut labore et dolore magna aliqua.</p></div>
    </div>
  </div>
</section>

<section class="clients">
  <div class="wrap">
    <div>
      <h3>WHAT OUR CLIENTS SAY</h3>
      <p>Lorem ipsum dolor sit amet, consectetur adipiscing elit, sed do eiusmod tempor incididunt ut labore et dolore.</p>
    </div>
    <div class="client-names"><span>Nexlane</span><span>Ovira</span><span>Tandru</span></div>
  </div>
</section>

<section class="testimonials">
  <div class="wrap">
    <div class="quote"><div class="headshot" role="img" aria-label="Headshot of a client"></div><div><h5>Ella Marsh, <span>Nexlane</span></h5><p>Lorem ipsum dolor sit amet, consectetur adipiscing elit, sed do eiusmod tempor incididunt.</p></div></div>
    <div class="quote"><div class="headshot" role="img" aria-label="Headshot of a client"></div><div><h5>Tom Reid, <span>Ovira</span></h5><p>Lorem ipsum dolor sit amet, consectetur adipiscing elit, sed do eiusmod tempor incididunt.</p></div></div>
    <div class="quote"><div class="headshot" role="img" aria-label="Headshot of a client"></div><div><h5>Nina Cole, <span>Tandru</span></h5><p>Lorem ipsum dolor sit amet, consectetur adipiscing elit, sed do eiusmod tempor incididunt.</p></div></div>
  </div>
</section>

<footer class="site-footer">
  <div class="wrap">
    <div class="links">Digital Marketing<br>Quorvo Promoline<br>Chatterlane Advertising<br>Search Engine Optimisation (SEO)<br>Website Hosting<br>Newsletter Management</div>
    <div class="links links-short">About<br>Contact<br>Privacy Policy<br>Terms &amp; Conditions<br>FAQ</div>
    <div class="company">
      <div class="brand"><span class="brand-dot"></span>BrightCrest</div>
      <p>BrightCrest, 14 Marlow Close, Eastmere,<br>Hollowshire, ZZ9 4QT<br>Tel: 01632 960481<br>info@brightcrest-demo.co.uk</p>
      <div class="socials"><i></i><i></i><i></i></div>
    </div>
    <div class="map" role="img" aria-label="Location map of the office in Eastmere">
      <svg width="16" height="22" viewBox="0 0 16 22"><path d="M8 0C3.6 0 0 3.5 0 7.8 0 13.5 8 22 8 22s8-8.5 8-14.2C16 3.5 12.4 0 8 0z" fill="#c0392b"/><circle cx="8" cy="8" r="3" fill="#fff"/></svg>
    </div>
  </div>
</footer>
<div class="bottom-bar"><div class="wrap"><span>Copyright 2016 BrightCrest. All rights reserved.</span><span>Web design by BrightCrest</span></div></div>

</body>
</html>
```